Create the ONLY Supplement line for Male Entrepreneurs! (Veltro Prime MD)

I need a label designed for a new supplement brand that I am launching.

There are five products so need a design that I can simply change the wording for each individual product

The brand name is called veltro prime MD. The focus is male entrepreneurial health.

Target audience is men 35 to 55.

Concepts: the healthier you are in body the more money you will make in business.

Concept to copy: I want to make a clean minimalistic label mimicking Dallamore MD (google it and you'll see what I mean)

Target Market(s)

male entrepreneurs 35-55

Industry/Entity Type

Health Supplement

Colors

Designer to choose colors to be used in the design.

Requirements
Must have
• Modern classy design, similar to Dallamore MD.
Nice to have
• Highlight that the supplement is Doctor Approved.
Should not have
• No loud colors. Present it as high class.

```html
<!DOCTYPE html>
<html lang="en">
<head>
<meta charset="utf-8">
<title>Veltro Prime MD – Health Supplement Label</title>
<link rel="stylesheet" href="https://fonts.googleapis.com/css2?family=Crimson+Pro:wght@400&family=Arimo:wght@700&display=swap">
<style>
  :root {
    --label-bg: #f0eee9;
    --frame: #4a4a4a;
    --burgundy: #5c2526;
    --ink: #111111;
    --ink-soft: #2b2b2b;
    --accent-soft: #ece2c5;
  }
  html, body {
    margin: 0;
    padding: 0;
    width: 1130px;
    height: 1200px;
    overflow: hidden;
    background: var(--label-bg);
  }
  .label {
    position: relative;
    width: 1130px;
    height: 1200px;
    box-sizing: border-box;
    border: 2px solid var(--frame);
    background: var(--label-bg);
    overflow: hidden;
  }
  .corner-accent {
    position: absolute;
    inset: 0;
    width: 100%;
    height: 100%;
  }
  .text {
    position: absolute;
    margin: 0;
    white-space: nowrap;
    font-weight: 400;
  }
  .brand-name {
    left: 128px;
    top: 92px;
    font-family: "Crimson Pro", serif;
    font-size: 112px;
    line-height: 1;
    color: var(--burgundy);
  }
  .product-type {
    left: 128px;
    top: 356px;
    font-family: "Crimson Pro", serif;
    font-size: 88px;
    line-height: 1;
    color: var(--ink);
  }
  .tagline {
    left: 128px;
    top: 462px;
    font-family: "Crimson Pro", serif;
    font-size: 52px;
    line-height: 1;
    color: var(--ink);
  }
  .divider {
    position: absolute;
    left: 132px;
    top: 669px;
    width: 882px;
    height: 12px;
    background: var(--burgundy);
  }
  .ingredients {
    left: 132px;
    top: 692px;
    font-family: "Crimson Pro", serif;
    font-size: 44px;
    line-height: 52px;
    color: var(--ink-soft);
  }
  .count {
    left: 128px;
    top: 848px;
    font-family: "Arimo", sans-serif;
    font-weight: 700;
    font-size: 42px;
    line-height: 1;
    color: var(--burgundy);
  }
  .approval {
    left: 128px;
    top: 1036px;
    font-family: "Arimo", sans-serif;
    font-weight: 700;
    font-size: 42px;
    line-height: 1;
    color: var(--burgundy);
  }
</style>
</head>
<body>
  <main class="label">
    <svg class="corner-accent" viewBox="0 0 1130 1200" role="img" aria-label="Faint diagonal stripe pattern in soft cream across the lower right corner">
      <defs>
        <linearGradient id="accentFade" x1="0" y1="0" x2="1" y2="1">
          <stop offset="0" stop-color="var(--accent-soft)" stop-opacity="0.25"/>
          <stop offset="1" stop-color="var(--accent-soft)" stop-opacity="0.9"/>
        </linearGradient>
      </defs>
      <polygon points="300,1200 1130,370 1130,1200" fill="url(#accentFade)"/>
    </svg>

    <h1 class="text brand-name">Veltro Prime MD</h1>
    <h2 class="text product-type">Health Supplement</h2>
    <p class="text tagline">for male entrepreneurial health</p>

    <div class="divider"></div>

    <p class="text ingredients">Ingredients: DMAE, Omega-3,<br>Evening Primrose Oil</p>
    <p class="text count">30 softgel capsules</p>
    <p class="text approval">This supplement is Doctor Approved</p>
  </main>
</body>
</html>
```